Flyer für eine Imkerei
Wunderbare unkomplizierte Zusammenarbeit mit einem tollen Designer. Extrem gutes Verständnis der Grundidee, super flexibles einarbeiten eigener Verbesserungsvorschläge - einfach sehr kompetent! Danke dafür.
Zielgruppe
Ich bin Hobbyimker mit einer sehr kleinen Imkerei im Dorf. Ich biete lokalen Honig an. Der Flyer soll ein Infoflyer für Kunden und evt. Neukunden sein.
Aufgabenstellung
Bitte im Wickelfalz hochkant A4, (gefaltet also 99x210). Textbausteine sind als Datei angehängt. Bitte nur den Text nutzen, nicht Schriftgröße, Schritart etc. Ebenso ist eigenes Bildmaterial vorhanden. Ich würde mich über ein edles aber schlicht modernes Design freuen. Das Design darf gern Honigwaben (Hexagon) als Grundidee beinhalten. Bevorzugte Farbtöne sind schwarz, gold, gelb, orange (honigfarben) bis Weinrot (siehe Honigetikett auf dem Foto).

```html
<!DOCTYPE html>
<html lang="de">
<head>
<meta charset="utf-8">
<title>Flyer Imkerei – Feinster Honig aus dem Saaletal</title>
<link href="https://fonts.googleapis.com/css2?family=Lora:wght@600;700&family=Source+Serif+4:wght@400;600&family=Allura&display=swap" rel="stylesheet">
<style>
  :root{
    --honey:#eea21a;
    --honey-deep:#d98c0c;
    --forest:#1f5a38;
    --ink:#4b2f1c;
    --paper:#fbfaf7;
    --fold:#ecebe6;
    --backdrop:#a4a8ad;
    --photo-green:#4f7a34;
    --photo-brown:#8a5a2c;
    --photo-yellow:#e8c22a;
  }
  *{box-sizing:border-box;margin:0;padding:0}
  html,body{width:1200px;height:686px;overflow:hidden}
  body{background:var(--backdrop);font-family:"Source Serif 4",Georgia,serif;color:var(--ink);position:relative}
  .sheet{position:absolute;top:135px;width:588px;height:416px;background:var(--paper);display:flex;box-shadow:0 6px 18px rgba(0,0,0,.18)}
  .sheet--inside{left:8px}
  .sheet--outside{left:604px}
  .panel{position:relative;width:196px;height:100%;padding:14px 13px;overflow:hidden;border-right:1px solid var(--fold)}
  .panel:last-child{border-right:none}
  h2{font-family:"Lora",Georgia,serif;font-weight:700;line-height:1.02}
  .title-honey{color:var(--honey);font-size:19px}
  .title-forest{color:var(--forest);font-size:18px}
  .subtitle{font-family:"Lora",serif;font-weight:700;color:var(--honey);font-size:13px;line-height:1.05;margin:6px 0 8px}
  h3{font-family:"Lora",serif;font-weight:700;color:var(--forest);font-size:9px;line-height:1.1;margin:7px 0 3px}
  p{font-size:6.3px;line-height:1.35}
  p + p{margin-top:4px}
  .hex-field{position:absolute;background:var(--honey)}
  .sketch{position:absolute;background:rgba(139,90,44,.18);border-radius:3px}
  .photo{border:2px solid var(--honey)}
  .row{display:flex;gap:5px;align-items:flex-start}
  .row p{flex:1}
  .fact{display:flex;gap:5px}
  .fact-label{font-family:"Lora",serif;font-weight:700;color:var(--forest);font-size:8px;line-height:1.05;width:34px;flex:none}
  .center{text-align:center}
  .script{font-family:"Allura",cursive;color:var(--forest);font-size:14px;line-height:1.1;text-align:center}
  .phone{font-family:"Lora",serif;font-weight:700;color:var(--forest);font-size:11px;text-align:center;margin-top:6px}
  .tagline{font-family:"Lora",serif;font-weight:600;color:var(--forest);font-size:7.5px;text-align:center}
  .dots{height:3px;margin:6px auto;width:70px;background:radial-gradient(circle,var(--honey) 1px,transparent 1.3px) 0 0/4px 3px}
  .address{font-family:"Lora",serif;font-weight:600;color:var(--forest);font-size:6px;text-align:center}
</style>
</head>
<body>

<section class="sheet sheet--inside">
  <article class="panel">
    <div class="hex-field" role="img" aria-label="Wabenmuster in Honiggelb" style="right:0;top:8px;width:70px;height:76px;clip-path:polygon(25% 0,100% 0,100% 100%,40% 90%,0 55%)"></div>
    <div class="sketch" role="img" aria-label="Zeichnung einer Biene" style="left:82px;top:38px;width:26px;height:18px"></div>
    <h2 class="title-honey">Unser<br>Honig</h2>
    <p style="margin-top:10px">Durch den festen Standort können mit zwei Honigernten im Jahr folgende Sorten angeboten werden, die den Geschmack der Saison einfangen:</p>
    <h3>Frühtracht –<br>cremig:</h3>
    <div class="row">
      <p>Gesammelt von den ersten Blüten des Jahres - vorwiegend Obstblüte und Raps. Für eine streichzarte Konsistenz wird dieser milde, blumige Honig vor dem Abfüllen fein-cremig gerührt.</p>
      <div class="photo" role="img" aria-label="Foto: Biene auf gelben Frühlingsblüten" style="width:88px;height:60px;background:linear-gradient(135deg,var(--photo-yellow),#6f8a2a)"></div>
    </div>
    <h3>Sommerblüte –<br>flüssig &amp; cremig:</h3>
    <p>Ein etwas kräftigerer und aromatischer Honig aus den Blüten des Hochsommers – vorwiegend Linde. Diesen Honig gibt es je nach Verfügbarkeit als flüssige Variante oder ebenfalls fein-cremig gerührt.</p>
    <p>Gut zu wissen: Echter Honig kann kristallisieren. Das ist ein natürlicher Prozess und ein Zeichen für hohe Qualität. Im Wasserbad bei maximal 40°C wird er schonend wieder flüssig. Honig bitte kühl, trocken und dunkel lagern.</p>
  </article>

  <article class="panel">
    <div class="sketch" role="img" aria-label="Zeichnung einer Biene" style="right:24px;top:16px;width:30px;height:26px"></div>
    <h2 class="title-forest">Warum<br>regional?</h2>
    <div class="subtitle">Gutes für Sie und unsere Heimat</div>
    <h3>1. Für die Natur vor unserer Haustür</h3>
    <p>Unsere Bienen bestäuben unzählige Pflanzen im Saaletal und sorgen so für den Erhalt der Artenvielfalt.</p>
    <h3>2. Absolute Transparenz</h3>
    <p>Keine langen Transportwege, keine undurchsichtigen Lieferketten. Der Honig kommt direkt vom Bienenstock im Wald in Ihr Glas. Der Erlös kommt zu 100% unserer Imkerei zugute.</p>
    <h3>3. Der Geschmack der Heimat</h3>
    <p>Jeder Löffel fängt den einzigartigen Geschmack der vielfältigen lokalen Pflanzenwelt des Saaletals ein.</p>
    <h3>4. Geprüfte Qualität</h3>
    <p>Unser Honig wird regelmäßig in einem Fachlabor auf Qualität und Zusammensetzung untersucht. Die Analyse der Pollen bestätigt dabei die botanische und geografische Herkunft – eine Garantie für echten Honig aus der Region.</p>
  </article>

  <article class="panel">
    <h2 class="title-honey" style="font-size:17px">Faszinierende</h2>
    <h2 class="title-forest" style="font-size:16px">Bienenwelt</h2>
    <div class="fact" style="margin-top:6px">
      <div>
        <div class="fact-label">Wuss-<br>ten Sie<br>schon?</div>
        <p style="margin-top:5px">Bienen sind echte Vielflieger! Für Ihr 500g-Glas Honig legen sie eine</p>
      </div>
      <div class="photo" role="img" aria-label="Foto: dicht gedrängte Bienen auf der Wabe" style="flex:1;height:98px;background:linear-gradient(135deg,#b07a3c,var(--photo-brown))"></div>
    </div>
    <p style="margin-top:4px">Flugstrecke hin, die dreimal um die Erde reicht. Sie verschenken ihr Lebenswerk! Eine Biene produziert in ihrem ganzen Leben nur etwa einen halben Teelöffel Honig. Genießen Sie den Honig bewusst – es steckt viel Arbeit drin!</p>
    <p>Im Bienenstock regiert eine knallharte Chefin! Im Sommer legt die Königin bis zu 2.000 Eier pro Tag.</p>
    <div class="hex-field" role="img" aria-label="Wabenmuster in Honiggelb" style="left:0;right:0;bottom:0;height:110px;clip-path:polygon(0 70%,55% 35%,100% 0,100% 100%,0 100%)"></div>
    <div class="photo" role="img" aria-label="Foto: gestapelte Gläser Blütenhonig" style="position:absolute;left:8px;bottom:26px;width:92px;height:64px;border:none;background:linear-gradient(160deg,#f2b33a,#b8661a)"></div>
  </article>
</section>

<section class="sheet sheet--outside">
  <article class="panel" style="padding-top:0">
    <div class="photo" role="img" aria-label="Foto: Bienenbeuten auf einer sonnigen Wiese am Waldrand" style="margin:0 -13px;height:120px;border:none;background:linear-gradient(180deg,#5e84b8 0,var(--photo-green) 45%,#3d6424)"></div>
    <div class="sketch" role="img" aria-label="Zeichnung eines Honiglöffels" style="left:70px;top:126px;width:16px;height:20px"></div>
    <h2 class="title-forest" style="font-size:13px;margin-top:26px">Über uns</h2>
    <p style="font-family:'Lora',serif;font-weight:700;color:var(--forest);font-size:7px;margin-top:2px">Herzlich willkommen in unserer kleinen Imkerei im schönen Saaletal!</p>
    <p style="margin-top:5px">Von der sorgsamen Pflege der sensiblen Bienenvölker über die Honigernte bis hin zum fertig etikettierten Glas wird jeder Arbeitsschritt persönlich vor Ort mit größter Sorgfalt ausgeführt, um ein reines und unverfälschtes Naturprodukt zu garantieren.</p>
    <h3>Natürlich &amp; schonend</h3>
    <p>Wir betreiben eine sanfte und wesensgemäße Bienenhaltung. Die Bienenstöcke haben einen festen Standort auf einer sonnigen Waldlichtung. Sie werden im Saisonverlauf nicht transportiert, sondern sammeln den Nektar der Pflanzen, die hier im Saaletal ganz natürlich saisonal blühen. Das garantiert einen authentischen Honig aus unserer Heimat.</p>
    <div class="hex-field" role="img" aria-label="Wabenmuster in Honiggelb" style="left:0;bottom:30px;width:14px;height:90px"></div>
  </article>

  <article class="panel" style="padding-top:0">
    <div class="hex-field" role="img" aria-label="Wabenmuster in Honiggelb mit Zeichnung eines Honigglases" style="left:-1px;right:0;top:0;height:62px;clip-path:polygon(0 0,100% 0,100% 40%,60% 70%,0 100%)"></div>
    <h2 class="title-forest" style="font-size:10px;margin-top:74px;text-align:center">Probieren Sie selbst!</h2>
    <p class="center" style="margin-top:4px">Wurde Ihre Neugier geweckt? Dann freuen wir uns, wenn Sie den reinen Geschmack unseres lokalen Produktes probieren möchten. Unser Honig ist vor Ort erhältlich.</p>
    <p class="center" style="margin-top:8px">Für Bestellungen und Abholungen erreichen Sie uns unter:</p>
    <div class="phone">Telefonnummer</div>
    <div class="row" style="margin:16px -6px 0;gap:3px">
      <div role="img" aria-label="Foto: verdeckelte Honigwabe im Rähmchen" style="flex:1;height:74px;background:linear-gradient(135deg,#e8a83a,#9c6a2c)"></div>
      <div role="img" aria-label="Foto: Bienen auf den Rähmchen eines offenen Stocks" style="flex:1;height:74px;background:linear-gradient(135deg,#c9b48a,#5a4630)"></div>
    </div>
    <div class="sketch" role="img" aria-label="Zeichnung einer Blüte" style="left:86px;top:312px;width:22px;height:18px"></div>
    <div class="script" style="margin-top:44px">Schauen Sie gern vorbei.<br>Wir freuen uns auf Sie!</div>
  </article>

  <article class="panel">
    <h2 class="title-honey" style="font-size:19px;margin:22px 0 0 8px">Feinster<br>Honig<br>aus dem<br>Saaletal</h2>
    <div class="hex-field" role="img" aria-label="Wabenmuster in Honiggelb mit gezeichneten Blüten und Bienen" style="right:0;top:150px;width:120px;height:110px;clip-path:polygon(20% 20%,70% 0,100% 10%,100% 100%,35% 95%,0 60%)"></div>
    <div class="sketch" role="img" aria-label="Zeichnung einer Biene" style="left:14px;top:170px;width:24px;height:22px"></div>
    <div class="sketch" role="img" aria-label="Zeichnung einer Biene" style="left:120px;top:292px;width:24px;height:18px"></div>
    <div style="position:absolute;left:0;right:0;bottom:44px">
      <div class="tagline">Natürlich, Regional &amp; Direkt</div>
      <div class="dots"></div>
      <div class="address">Name Ort Straße</div>
    </div>
  </article>
</section>

</body>
</html>
```